Infoblatt
Zielgruppe
Talentförderung, Personalentwicklung, Beratung von Personalabteilungen
Zielgruppe: Personaler, HR Verantwortliche
Aufgabenstellung
Es geht um einen "One-Pager", der auf einem Kongress ausgelegt werden soll und in Kurzform einen Überblick über unser Unternehmen und unser Angebot informieren soll.
Wir haben Visitenkarten auf Recyclingpapier und möchten das Blatt konsistent auf das gleiche Papier drucken lassen, daher einfarbig schwarz. Format DIN A4 Hoch.
IDEE: Vom Stil wie eine Infografik aufbauen
TYPO: unser LOGO ist BEBAS NEUE und unsere Schrift Helvetica

```html
<!DOCTYPE html>
<html lang="de">
<head>
<meta charset="utf-8">
<title>KERNWERK – Infoblatt</title>
<link rel="stylesheet" href="https://fonts.googleapis.com/css2?family=Bebas+Neue&family=Arimo:wght@400;700&display=swap">
<style>
  :root {
    --ink: #111111;
    --canvas: #e4e4e4;
    --paper-light: #f2f2f2;
    --paper-mid: #cfcfcf;
    --paper-dark: #9d9d9d;
    --ring-base: #a9a9a9;
    --ring-dark: #8e8e8e;
    --ring-light: #c6c6c6;
    --rule: #1a1a1a;
  }
  * { margin: 0; padding: 0; box-sizing: border-box; }
  html, body { width: 1200px; height: 1200px; overflow: hidden; background: var(--canvas); }
  .stage { position: relative; width: 1200px; height: 1200px; font-family: "Arimo", Helvetica, Arial, sans-serif; color: var(--ink); }

  .sheet { position: absolute; overflow: hidden; }
  .sheet--front { left: 60px; top: 66px; width: 778px; height: 1104px; }
  .sheet--back { left: 838px; top: 463px; width: 344px; height: 569px; }

  .backdrop { position: absolute; inset: 0; }
  .sheet--front .backdrop {
    background:
      radial-gradient(ellipse 60% 25% at 45% 92%, #f7f7f7 0%, rgba(247,247,247,0) 70%),
      linear-gradient(180deg, #dcdcdc 0%, #d2d2d2 35%, #e6e6e6 70%, #c9c9c9 100%);
  }
  .sheet--back .backdrop {
    background:
      radial-gradient(ellipse 70% 30% at 70% 80%, #f4f4f4 0%, rgba(244,244,244,0) 70%),
      linear-gradient(180deg, #d9d9d9 0%, #c6c6c6 50%, #bdbdbd 100%);
  }

  .graphics { position: absolute; inset: 0; }

  .brand { position: absolute; font-family: "Bebas Neue", Impact, sans-serif; font-weight: 400; line-height: 1; color: var(--ink); }
  .sheet--front .brand { right: 42px; top: 38px; font-size: 58px; letter-spacing: 0.5px; }
  .sheet--back .brand { right: 20px; top: 124px; font-size: 52px; letter-spacing: 0.5px; }

  .block { position: absolute; }
  .block__title { font-family: "Bebas Neue", Impact, sans-serif; font-weight: 400; font-size: 56px; line-height: 0.95; }
  .block__sub { font-family: "Bebas Neue", Impact, sans-serif; font-weight: 400; font-size: 30px; line-height: 1; margin-top: 2px; }
  .block__text { font-size: 15px; line-height: 19px; }
  .block__text strong { font-weight: 700; }
  .block__text p + p { margin-top: 19px; }

  .block--credo { left: 35px; top: 110px; }
  .block--credo .block__text { margin-top: 26px; width: 450px; }
  .block--mehrwert { left: 38px; top: 322px; }
  .block--mehrwert .block__text { margin-top: 28px; width: 220px; }
  .block--mission { left: 276px; top: 738px; }
  .block--mission .block__text { margin-top: 26px; width: 460px; }

  .contact { position: absolute; right: 18px; top: 500px; text-align: right; font-size: 8.5px; line-height: 10.5px; }
</style>
</head>
<body>
<main class="stage">

  <section class="sheet sheet--front">
    <div class="backdrop" role="img" aria-label="Blurred black-and-white photo of a workshop table with flipchart paper and markers"></div>
    <svg class="graphics" width="778" height="1104" viewBox="0 0 778 1104">
      <defs>
        <clipPath id="front-photo-clip"><circle cx="529" cy="501" r="152"/></clipPath>
        <radialGradient id="front-photo-fill" cx="45%" cy="55%" r="60%">
          <stop offset="0%" stop-color="#5a5a5a"/>
          <stop offset="55%" stop-color="#8a8a8a"/>
          <stop offset="100%" stop-color="#d4d4d4"/>
        </radialGradient>
      </defs>
      <circle cx="529" cy="501" r="165" fill="none" stroke="var(--ring-base)" stroke-width="26"/>
      <circle cx="529" cy="501" r="165" fill="none" stroke="var(--ring-dark)" stroke-width="26"
              stroke-dasharray="259 1037" transform="rotate(-90 529 501)"/>
      <circle cx="529" cy="501" r="165" fill="none" stroke="var(--ring-light)" stroke-width="26"
              stroke-dasharray="190 1037" transform="rotate(100 529 501)"/>
      <g clip-path="url(#front-photo-clip)">
        <rect x="370" y="340" width="320" height="320" fill="url(#front-photo-fill)"
              role="img" aria-label="Blurred photo of people in a workshop discussion"/>
      </g>
      <polyline points="35,197 644,197 644,362" fill="none" stroke="var(--rule)" stroke-width="1.3"/>
      <line x1="38" y1="417" x2="376" y2="417" stroke="var(--rule)" stroke-width="1.3"/>
      <polyline points="570,664 570,827 276,827" fill="none" stroke="var(--rule)" stroke-width="1.3"/>
    </svg>

    <div class="brand">KERNWERK</div>

    <article class="block block--credo">
      <h2 class="block__title">Credo</h2>
      <h3 class="block__sub">Woran wir glauben:</h3>
      <div class="block__text">
        <p>Wir glauben, dass sich persönliche und ökonomische Werte ergänzen - mehr noch, dass sie langfristig nicht ohne einander auskommen und dass sich emotionale Bindung als Mehrwert in Zahlen ausdrückt.</p>
      </div>
    </article>

    <article class="block block--mehrwert">
      <h2 class="block__title">Mehrwert</h2>
      <h3 class="block__sub">Was wir bieten:</h3>
      <div class="block__text">
        <p>Wir beraten Unternehmen im Rahmen der Talentförderung und helfen Jugendlichen auf dem Weg in ihr Berufsleben.</p>
        <p><strong>Für Unternehmen:</strong><br>Talentförderung &amp; Talent Management<br>Professionalisierung der Personalarbeit<br>Organisationsentwicklung<br>Potentialorientierte Mit-<br>arbeiterführung</p>
        <p><strong>Für die junge Generation:</strong><br>Berufsorientierung<br>Bewerbungscoaching</p>
      </div>
    </article>

    <article class="block block--mission">
      <h2 class="block__title">Mission</h2>
      <h3 class="block__sub">Was unser Handeln leitet:</h3>
      <div class="block__text">
        <p>Kundare heißt marktschreierisch anpreisen, hinters Licht führen, täuschen. Mandare heißt beauftragen, Vertrauen schenken. Wir legen großen Wert auf eine Beziehung, die Mandare, nicht Kundare entspricht. Für uns ist der partnerschaftliche Umgang mit unseren Mandanten das Fundament. Wir haben keine Kunden. Wir unterstützen Mandanten.</p>
      </div>
    </article>
  </section>

  <section class="sheet sheet--back">
    <div class="backdrop" role="img" aria-label="Soft black-and-white photo of chalk sticks on a table"></div>
    <svg class="graphics" width="344" height="569" viewBox="0 0 344 569">
      <circle cx="202" cy="227" r="90" fill="none" stroke="var(--ring-base)" stroke-width="14"/>
      <circle cx="202" cy="227" r="90" fill="none" stroke="var(--ring-light)" stroke-width="14"
              stroke-dasharray="140 566" transform="rotate(60 202 227)"/>
      <g class="team">
        <circle cx="30" cy="225" r="24" fill="#efefef" role="img" aria-label="Portrait of team member 1"/>
        <circle cx="79" cy="225" r="24" fill="#dedede" role="img" aria-label="Portrait of team member 2"/>
        <circle cx="135" cy="225" r="24" fill="#e6e6e6" role="img" aria-label="Portrait of team member 3"/>
        <circle cx="191" cy="225" r="24" fill="#f0f0f0" role="img" aria-label="Portrait of team member 4"/>
        <circle cx="247" cy="225" r="24" fill="#e2e2e2" role="img" aria-label="Portrait of team member 5"/>
      </g>
      <rect x="182" y="535" width="16" height="16" fill="#6a6a6a"/>
    </svg>

    <div class="brand">KERNWERK</div>

    <address class="contact" style="font-style:normal">
      Lindenhofweg 12<br>
      42103 Musterstadt<br>
      Fon: 0202.5550198<br>
      E-Mail: info@kernwerk-beratung.de<br>
      www.kernwerk-beratung.de
    </address>
  </section>

</main>
</body>
</html>
```